Marrowfell Website Concept

We would like a one page website. Please refer to the attached files for more information.

Please reference file attachment version 1.1.

```html
<!DOCTYPE html>
<html lang="en">
<head>
<meta charset="utf-8">
<title>Marrowfell Security</title>
<link rel="stylesheet" href="https://fonts.googleapis.com/css2?family=Arimo:ital,wght@0,400;1,700&family=Libre+Baskerville:wght@700&display=swap">
<style>
  :root {
    --ink: #111111;
    --navy: #1d3f5e;
    --sky: #bfdcec;
    --night: #0f2331;
    --field: #253d4b;
    --white: #ffffff;
  }
  * { margin: 0; padding: 0; box-sizing: border-box; }
  html, body { width: 853px; height: 1200px; overflow: hidden; background: var(--white); }
  body { position: relative; font-family: "Arimo", Arial, sans-serif; color: var(--ink); }

  .brand {
    position: absolute; left: 26px; top: 48px;
    display: flex; align-items: center; gap: 10px;
    font-family: "Libre Baskerville", Georgia, serif; font-weight: 700;
    font-size: 23px; letter-spacing: 1px; color: var(--navy);
  }
  .brand-dot { width: 26px; height: 26px; border-radius: 50%; background: var(--navy); }

  .intro {
    position: absolute; left: 0; top: 85px; width: 853px; height: 343px;
    background: var(--sky);
  }
  .intro-copy {
    position: absolute; left: 131px; top: 86px; width: 592px;
    text-align: center; font-size: 10.4px; line-height: 11.6px;
  }
  .intro-copy p + p { margin-top: 11.6px; }
  .intro-copy em { font-weight: 700; }

  .services { position: absolute; left: 0; top: 512px; width: 853px; text-align: center; }
  .section-title {
    font-family: "Libre Baskerville", Georgia, serif; font-weight: 700;
    font-size: 14px; letter-spacing: 0.3px; color: var(--navy);
  }
  .service-list { list-style: none; margin-top: 16px; font-size: 10.6px; line-height: 12.6px; }

  .register {
    position: absolute; left: 0; top: 686px; width: 853px; height: 514px;
    background: var(--night);
  }
  .register .section-title { position: absolute; left: 0; top: 83px; width: 853px; text-align: center; color: var(--white); font-size: 15px; }
  .form-row { position: absolute; left: 273px; width: 419px; height: 18px; }
  .form-row label {
    position: absolute; left: 0; top: 4px;
    font-size: 10.6px; color: var(--white);
  }
  .form-row .field {
    position: absolute; left: 165px; top: 0; width: 254px; height: 18px;
    border: 0; background: var(--field); color: var(--white);
    font: inherit; font-size: 10.6px; padding: 0 6px;
  }
  .form-row.message .field { height: 46px; resize: none; }
</style>
</head>
<body>
  <header class="brand"><span class="brand-dot"></span>MARROWFELL</header>

  <section class="intro">
    <div class="intro-copy">
      <p><em>Marrowfell Security, LLC</em> is a United States-based tier one security firm specializing in the protection of financial services professionals, executives and their families.&nbsp; We manage engagements resulting from general and specific threats throughout the United States and abroad on behalf of our domestic clients.&nbsp; We deliver our services exclusively through associates and contractors with United States special operations, secret service, CIA, or equivalent experience and training.&nbsp; We are one of only a handful of domestic security firms that offers scalable, tier one security services in every market in the United States.</p>
      <p>If you have a general or specific threat you would like to have assessed, it will be our privilege to evaluate your circumstances and provide you with an opinion of how to best address your security needs.&nbsp; Not all security circumstances require tier one professionals. It will be our pleasure to direct you to other firms in your market if you or we believe our service levels are not warranted.</p>
      <p>Our firm was created as the result of a specific threat to two of our founders following a private equity transaction with a hostile seller. If you are a transaction professional, executive or a high profile individual who is experiencing the fear and uncertainty of the risks associated with a general or specific security threat, it will be our privilege to help you manage this challenging process.</p>
    </div>
  </section>

  <section class="services">
    <h2 class="section-title">SERVICE OFFERINGS</h2>
    <ol class="service-list">
      <li>1. Threat Assessment</li>
      <li>2. Threat Avoidance Plan &amp; Dossier Creation</li>
      <li>3. Elite Executive Protection</li>
      <li>4. Threat Avoidance Plan &amp; Dossier Maintenance</li>
    </ol>
  </section>

  <section class="register">
    <h2 class="section-title">GET REGISTERED</h2>
    <form>
      <div class="form-row" style="top:131px"><label>First Name</label><input class="field" type="text"></div>
      <div class="form-row" style="top:156px"><label>Last Name</label><input class="field" type="text"></div>
      <div class="form-row" style="top:181px"><label>Home Phone</label><input class="field" type="tel"></div>
      <div class="form-row" style="top:206px"><label>Work Phone</label><input class="field" type="tel"></div>
      <div class="form-row" style="top:231px"><label>Cell Phone</label><input class="field" type="tel"></div>
      <div class="form-row" style="top:255px"><label>Email Address</label><input class="field" type="email"></div>
      <div class="form-row" style="top:280px"><label>Address</label><input class="field" type="text"></div>
      <div class="form-row" style="top:305px"><label>Address</label><input class="field" type="text"></div>
      <div class="form-row" style="top:330px"><label>City</label><input class="field" type="text"></div>
      <div class="form-row" style="top:355px"><label>State</label><input class="field" type="text"></div>
      <div class="form-row" style="top:380px"><label>Zip</label><input class="field" type="text"></div>
      <div class="form-row message" style="top:404px"><label>Message</label><textarea class="field"></textarea></div>
    </form>
  </section>
</body>
</html>
```